Website Design For Corben Hub Project

www.corbenhub-example.com.au

As the name suggests i would like to have a design for this website... the website is nothing to do with night life or parties, but it is do everything to do with being online all the time, being available 24/7.

all information needed regarding anything to do with this City and its businesses. so, Basically This will be an online business directory for local businesses. What i am looking for is a website that can display Business listings in a pleasant, lively, friendly, attitude that reflects the towns people, this city boasts with a largest inland city in Australia, and a local university to match, it has its own airport, malls, markets and supermarkets. This website directory/each business layout will be very similar to the ones on www.pelford-direct-example.com.au.

Wagga Wagga has a community of numerous backgrounds, cutlures, creeds and beliefs and religions to be a thriving one.

Therefore, i want the website to reflect its green hills and flowing rivers. The is a advertising point.

An online venue for the local and surrounding bussinesses to be found with a minimum amount of clicks and hassles. Essentially it is a business directory, but not just any directory you see online. I do not want it to look like the fastfind guides or nameline books. this website directory is specific to one location and its bussinesses are particular to that area. I want the website to almost have an emotion for that City, not just an army of black and white ants marching across the page.

Yours colours are you own imagination as long as it is visible and readable by majority of people; its colours are pleasant and not offensive to the eyes: i.e: not too bright, not too dark and depressing.

"corbenhub" is to be included in your website design.

Reason: The deadline has been extended as there are few nice concepts however they need to be a bit more clean in its layout, the color choices are not quite right, as well as the banners need to look more presentable. Thanks

Target Market(s)

The Target Market is Small to Medum Businesses to List their business online and Gen Y and Mums & dads looking for services in the city of Wagga Wagga

Industry/Entity Type

Business Directory

Requirements
Must have
• Search Bar
Social Media Widgets (ChumSpace, Plinko, Pocket sift)
Categories
Sliding Banners
Each Major Category Should have an image or a nice Icon representing the category

```html
<!DOCTYPE html>
<html lang="en">
<head>
<meta charset="utf-8">
<title>Corben Hub – Online Business Directory</title>
<link rel="stylesheet" href="https://fonts.googleapis.com/css2?family=Arimo:wght@400;700&family=PT+Sans+Narrow&family=Courgette&display=swap">
<style>
:root{
  --orange:#ee7d14;
  --orange-dark:#b34a06;
  --title:#b4470b;
  --ink:#3a3a3a;
  --muted:#555;
  --rule:#d6d6d6;
  --page:#ffffff;
  --bg:#eeeeee;
  --star:#f3b01c;
  --star-off:#d9d9d9;
}
*{box-sizing:border-box;margin:0;padding:0}
html,body{width:1105px;height:1200px;overflow:hidden}
body{background:var(--bg);font-family:"Arimo",Arial,sans-serif;color:var(--ink);position:relative}
.abs{position:absolute}
.page{left:157px;top:0;width:790px;height:1155px;background:var(--page);box-shadow:0 3px 8px rgba(0,0,0,.25)}
.topbar{left:157px;top:0;width:790px;height:18px;background:linear-gradient(#fafafa,#dcdcdc);border-bottom:1px solid #ccc}
.welcome{left:186px;top:4px;font-size:9px;color:var(--orange-dark)}
.brand{left:178px;top:30px;font-size:40px;font-weight:700;color:var(--orange);display:flex;align-items:center;gap:12px;letter-spacing:.5px}
.brand .mark{width:22px;height:22px;background:var(--orange)}
.nav{top:26px;display:flex;flex-direction:column;align-items:center;font-size:11px;color:#666;gap:4px}
.nav svg{width:26px;height:24px;fill:#777}
.search{left:257px;top:108px;width:616px;height:56px;border-radius:6px;background:linear-gradient(#f4932c,#d86a0a 55%,#a84305);box-shadow:0 2px 4px rgba(0,0,0,.35)}
.search .label{position:absolute;top:16px;font-family:"Courgette",cursive;color:#fff;font-size:16px}
.search .field{position:absolute;top:16px;height:26px;background:#fff;border-radius:5px}
.banner{left:165px;top:182px;width:774px;height:77px;border-radius:5px;border:1px solid #ddd;background:linear-gradient(100deg,#f1f1f1 0%,#f7f7f7 27%,#bdbdbd 30%,#ffffff 33%,#cfcfcf 36%,#f5f5f5 42%,#ececec 100%);box-shadow:inset 0 -2px 3px rgba(0,0,0,.08)}
.banner p{font-family:"PT Sans Narrow",sans-serif;font-size:22px;color:var(--title);text-align:center;margin-top:26px}
.ribbon{left:157px;width:183px;height:26px;background:var(--orange);clip-path:polygon(0 0,100% 0,88% 50%,100% 100%,0 100%);color:#fff;font-size:13px;display:flex;align-items:center;padding-left:14px;gap:8px}
.ribbon .ico{width:20px;height:20px;border-radius:3px;background:linear-gradient(#ffe2a8,#5b7fd1)}
.ribbon.lg{font-size:16px}
.alpha{left:375px;top:277px;width:538px;height:17px;border-radius:3px 9px 9px 3px;background:linear-gradient(#f7f7f7,#cfcfcf);display:flex;justify-content:space-around;align-items:center;padding:0 10px;font-size:10px;color:#333;letter-spacing:.5px}
.alpha .on{color:var(--orange)}
.cat{display:flex;align-items:center;font-size:10px;color:#333;gap:0}
.cat .ico{width:28px;height:24px;border-radius:4px;margin-right:16px}
.vsep{width:2px;background:linear-gradient(rgba(0,0,0,0),rgba(0,0,0,.07),rgba(0,0,0,0))}
.hr{height:1px;background:var(--rule)}
.sub{font-size:10px;color:#333;display:flex;align-items:center}
.sub::before{content:"";border-left:6px solid #333;border-top:4px solid transparent;border-bottom:4px solid transparent;margin-right:8px}
.sub.on::before{border-left-color:var(--orange)}
.about{left:563px;top:564px;width:372px;font-size:9.2px;line-height:19px;color:#444}
.results{left:182px;top:784px;font-size:14px;color:#333}
.item{left:182px;width:745px}
.item h3{font-weight:400;font-size:12.5px;color:var(--title)}
.item p{font-size:8.7px;line-height:19px;color:#444;margin-top:4px;width:735px}
.rate{left:731px;display:flex;align-items:center;gap:12px;font-size:10px;color:#444}
.rate svg{width:78px;height:14px}
.copy{left:0;width:1105px;top:1173px;text-align:center;font-size:9px;color:#333}
</style>
</head>
<body>
<svg width="0" height="0" style="position:absolute">
  <defs>
    <symbol id="star" viewBox="0 0 20 20"><polygon points="10,1 12.6,7 19,7.4 14,11.6 15.6,18 10,14.5 4.4,18 6,11.6 1,7.4 7.4,7"/></symbol>
    <linearGradient id="half"><stop offset="50%" stop-color="#f3b01c"/><stop offset="50%" stop-color="#d9d9d9"/></linearGradient>
    <symbol id="stars" viewBox="0 0 78 14">
      <use href="#star" x="0" width="14" height="14" fill="#f3b01c"/>
      <use href="#star" x="16" width="14" height="14" fill="url(#half)"/>
      <use href="#star" x="32" width="14" height="14" fill="none" stroke="#cfcfcf"/>
      <use href="#star" x="48" width="14" height="14" fill="none" stroke="#cfcfcf"/>
      <use href="#star" x="64" width="14" height="14" fill="none" stroke="#cfcfcf"/>
    </symbol>
  </defs>
</svg>

<div class="abs page"></div>
<div class="abs topbar"></div>
<div class="abs welcome">Welcome to corben hub</div>

<header>
  <div class="abs brand"><span class="mark"></span>Corben Hub</div>
  <nav>
    <div class="abs nav" style="left:678px"><svg viewBox="0 0 26 24"><path d="M13 2 2 12h3v10h6v-6h4v6h6V12h3z"/></svg>Home</div>
    <div class="abs nav" style="left:733px"><svg viewBox="0 0 26 24"><circle cx="9" cy="7" r="4"/><circle cx="18" cy="7" r="4"/><rect x="3" y="13" width="20" height="9" rx="4"/></svg>About Us</div>
    <div class="abs nav" style="left:806px"><svg viewBox="0 0 26 24"><path d="M3 3h10l11 11-9 9L3 12z" fill="none" stroke="#777" stroke-width="3"/><circle cx="8" cy="8" r="2"/></svg>Categories</div>
    <div class="abs nav" style="left:884px"><svg viewBox="0 0 26 24"><path d="M2 9c3-6 19-6 22 0l-4 3-3-3H9L6 12z"/><rect x="5" y="12" width="16" height="10" rx="2"/></svg>Contact</div>
  </nav>
</header>

<form class="abs search" role="search">
  <span class="label" style="left:24px">Search</span>
  <span class="field" style="left:80px;width:276px"></span>
  <span class="label" style="left:367px">Category</span>
  <span class="field" style="left:438px;width:126px"></span>
</form>

<section class="abs banner"><p>Corben Hub Online Classifieds for small scale to big companies Advertisings ....</p></section>

<div class="abs ribbon lg" style="top:271px">Business Searches</div>
<div class="abs alpha"><span>0 - 9</span><span class="on">A</span><span>B</span><span>C</span><span>D</span><span>E</span><span>F</span><span>G</span><span>H</span><span>I</span><span>J</span><span>K</span><span>L</span><span>M</span><span>N</span><span>O</span><span>P</span><span>Q</span><span>R</span><span>S</span><span>T</span><span>U</span><span>V</span><span>W</span><span>X</span><span>Y</span><span>Z</span></div>

<div class="abs vsep" style="left:410px;top:305px;height:195px"></div>
<div class="abs vsep" style="left:674px;top:305px;height:195px"></div>

<div class="abs cat" style="left:190px;top:321px"><span class="ico" role="img" aria-label="Art brushes icon" style="background:linear-gradient(#6d7fd4,#d94b3a)"></span>Art &amp; Antiques</div>
<div class="abs cat" style="left:190px;top:355px"><span class="ico" role="img" aria-label="Car icon" style="background:linear-gradient(#e34141,#9d1414)"></span>Automobiles</div>
<div class="abs cat" style="left:190px;top:389px"><span class="ico" role="img" aria-label="Books icon" style="background:linear-gradient(#4a6aa8,#1f2f55)"></span>Books &amp; Publications</div>
<div class="abs cat" style="left:190px;top:422px"><span class="ico" role="img" aria-label="Briefcase icon" style="background:linear-gradient(#c56a2b,#6e3110)"></span>Business Opportunities</div>
<div class="abs cat" style="left:190px;top:456px"><span class="ico" role="img" aria-label="Chemistry flask icon" style="background:linear-gradient(#bfe3f7,#2b7fc4)"></span>Chemicals</div>

<div class="abs cat" style="left:462px;top:321px"><span class="ico" role="img" aria-label="Shirt icon" style="background:linear-gradient(#e25050,#9e1b1b)"></span>Clothing &amp; Accessories</div>
<div class="abs cat" style="left:462px;top:355px"><span class="ico" role="img" aria-label="Computer icon" style="background:linear-gradient(#4a86d9,#1b3d7a)"></span>Computers</div>
<div class="abs cat" style="left:462px;top:389px"><span class="ico" role="img" aria-label="Graduation icon" style="background:linear-gradient(#f0c08a,#2a4b8a)"></span>Education &amp; Learning</div>
<div class="abs cat" style="left:462px;top:422px"><span class="ico" role="img" aria-label="Light bulb icon" style="background:linear-gradient(#e6f2fb,#9fbfd8)"></span>Electronics</div>
<div class="abs cat" style="left:462px;top:456px"><span class="ico" role="img" aria-label="Dice icon" style="background:linear-gradient(#fafafa,#9a9a9a)"></span>Entertienment</div>

<div class="abs cat" style="left:724px;top:321px"><span class="ico" role="img" aria-label="Sale tag icon" style="background:linear-gradient(#a8dc63,#3f9a23)"></span>Events for sale</div>
<div class="abs cat" style="left:724px;top:355px"><span class="ico" role="img" aria-label="Furniture icon" style="background:linear-gradient(#d9ecf8,#6fa4cf)"></span>Furniture</div>
<div class="abs cat" style="left:724px;top:389px"><span class="ico" role="img" aria-label="Health icon" style="background:linear-gradient(#f4e07a,#7ea2c9)"></span>Health</div>
<div class="abs cat" style="left:724px;top:422px"><span class="ico" role="img" aria-label="Tools icon" style="background:linear-gradient(#f5c938,#5a5a5a)"></span>Heavy goods &amp; Machines</div>
<div class="abs cat" style="left:724px;top:456px"><span class="ico" role="img" aria-label="Server icon" style="background:linear-gradient(#c9d6e2,#5d7188)"></span>IT &amp; ITES</div>

<svg class="abs" style="left:893px;top:495px" width="22" height="10" viewBox="0 0 22 10"><polygon points="8,0 0,5 8,10" fill="#bbb"/><polygon points="14,0 22,5 14,10" fill="#bbb"/></svg>

<div class="abs hr" style="left:168px;top:513px;width:760px"></div>

<div class="abs ribbon" style="top:525px"><span class="ico" role="img" aria-label="Art brushes icon"></span>Art &amp; Antiques</div>
<div class="abs ribbon" style="top:525px;left:544px"><span class="ico" role="img" aria-label="Community icon" style="background:linear-gradient(#ffd08a,#d9661a)"></span>About CorbenHub</div>
<div class="abs vsep" style="left:544px;top:552px;height:170px"></div>

<div class="abs sub on" style="left:185px;top:573px">Antiques</div>
<div class="abs sub" style="left:185px;top:598px">Art Classes</div>
<div class="abs sub" style="left:185px;top:623px">Art Stationery &amp; Accessories</div>
<div class="abs sub" style="left:185px;top:648px">galleries &amp; Exhibitions</div>
<div class="abs sub" style="left:185px;top:673px">Gift Articles</div>
<div class="abs sub" style="left:391px;top:573px">Glasses</div>
<div class="abs sub" style="left:391px;top:598px">Musical Instruments</div>
<div class="abs sub" style="left:391px;top:623px">Paintings &amp; Collectibles</div>
<div class="abs sub" style="left:391px;top:648px">Sculptures</div>

<p class="abs about">Lorem Ipsum is simply dummy text of the printing and typesetting industry. Lorem Ipsum has been the industry's standard dummy text ever since the 1500s, when an unknown printer took a galley of type and scrambled it to make a type specimen book. It has survived not only five centuries, but also the leap into electronic typesetting, remaining essentially unchanged. It was popularised in the 1960s with the release of Typefold sheets containing Lorem Ipsum passages, and more recently with desktop publishing software like Quillmark Layout including versions of Lorem Ipsum.</p>

<div class="abs hr" style="left:168px;top:727px;width:760px"></div>
<div class="abs ribbon" style="top:736px"><span class="ico" role="img" aria-label="Star listing icon" style="background:linear-gradient(#ffd34d,#3f6fc2)"></span>Listings</div>

<h2 class="abs results" style="font-weight:400">Results</h2>

<article class="abs item" style="top:809px"><h3>Lorem Ipsum is not simply random text</h3><p>It is a long established fact that a reader will be distracted by the readable content of a page when looking at its layout. The point of using Lorem Ipsum is that it has a more-or-less normal distribution of letters, as opposed to using 'Content here,</p></article>
<div class="abs rate" style="top:798px">Values<svg><use href="#stars"/></svg></div>
<div class="abs hr" style="left:168px;top:886px;width:760px"></div>

<article class="abs item" style="top:905px"><h3>Lorem Ipsum is not simply random text</h3><p>It is a long established fact that a reader will be distracted by the readable content of a page when looking at its layout. The point of using Lorem Ipsum is that it has a more-or-less normal distribution of letters, as opposed to using 'Content here,</p></article>
<div class="abs rate" style="top:894px">Values<svg><use href="#stars"/></svg></div>
<div class="abs hr" style="left:168px;top:966px;width:760px"></div>

<article class="abs item" style="top:985px"><h3>Lorem Ipsum is not simply random text</h3><p>It is a long established fact that a reader will be distracted by the readable content of a page when looking at its layout. The point of using Lorem Ipsum is that it has a more-or-less normal distribution of letters, as opposed to using 'Content here,</p></article>
<div class="abs rate" style="top:974px">Values<svg><use href="#stars"/></svg></div>
<div class="abs hr" style="left:168px;top:1048px;width:760px"></div>

<article class="abs item" style="top:1064px"><h3>Lorem Ipsum is not simply random text</h3><p>It is a long established fact that a reader will be distracted by the readable content of a page when looking at its layout. The point of using Lorem Ipsum is that it has a more-or-less normal distribution of letters, as opposed to using 'Content here,</p></article>
<div class="abs rate" style="top:1054px">Values<svg><use href="#stars"/></svg></div>

<footer class="abs copy">Copyright © 2011.www.corbenhub-example.com.au</footer>
</body>
</html>
```